Visitenkarten-Design für Persisches Restaurant
Zielgruppe
persisches Restaurant, suche ein Hochwertiges Design für internationale Kunden
Aufgabenstellung
möchte eine hochwertige und elegante visitenkarte
auf der Vorderseite sollte das Logo sein und auf der Rückseite Öffnungszeit, Adresse, Tel. E-Mail und homepage

```html
<!DOCTYPE html>
<html lang="de">
<head>
<meta charset="utf-8">
<title>Darvan – Visitenkarte</title>
<link href="https://fonts.googleapis.com/css2?family=Open+Sans:wght@400&family=Tinos:wght@400&display=swap" rel="stylesheet">
<style>
  :root{
    --page:#ffffff;
    --card-white:#ffffff;
    --card-grey:#6d6e71;
    --card-black:#141414;
    --ink:#231f20;
    --ink-light:#ffffff;
    --hours-ink:#1e1e1e;
  }
  html,body{margin:0;padding:0;}
  body{width:1200px;height:2507px;overflow:hidden;background:var(--page);position:relative;}
  .card{position:absolute;left:283px;width:633px;height:351px;box-shadow:0 6px 14px rgba(0,0,0,.35);}
  .card-front{top:269px;background:var(--card-white);}
  .card-back{top:714px;background:var(--card-grey);overflow:hidden;}
  .brand{position:absolute;left:0;right:0;top:150px;display:flex;justify-content:center;align-items:center;gap:12px;
    font-family:"Tinos",serif;font-size:40px;color:var(--ink);letter-spacing:1px;}
  .brand-dot{width:14px;height:14px;border-radius:50%;background:var(--ink);}
  .back-shape{position:absolute;inset:0;width:100%;height:100%;}
  .contact{position:absolute;font-family:"Tinos",serif;font-size:21px;color:var(--ink-light);line-height:27px;}
  .contact-row{position:absolute;left:36px;display:flex;align-items:center;white-space:nowrap;}
  .contact-row svg{width:13px;height:13px;margin-right:11px;fill:var(--ink-light);}
  .indent{padding-left:24px;}
  .hours{position:absolute;left:433px;top:26px;font-family:"Open Sans",sans-serif;font-size:19px;color:var(--hours-ink);line-height:26.7px;}
  .hours-row{display:flex;}
  .hours-day{width:49px;}
</style>
</head>
<body>
  <section class="card card-front">
    <div class="brand"><span class="brand-dot"></span><span>DARVAN</span></div>
  </section>

  <section class="card card-back">
    <svg class="back-shape" viewBox="0 0 532 295" preserveAspectRatio="none">
      <path d="M0 0 H112 C150 60 220 85 285 115 C345 145 345 230 318 295 H0 Z" fill="var(--card-black)"/>
    </svg>

    <div class="contact">
      <div class="contact-row" style="top:161px;">
        <svg viewBox="0 0 10 14"><path d="M5 0a5 5 0 0 0-5 5c0 4 5 9 5 9s5-5 5-9a5 5 0 0 0-5-5zm0 7a2 2 0 1 1 0-4 2 2 0 0 1 0 4z"/></svg>
        <span>Lindenhofweg 14</span>
      </div>
      <div class="contact-row indent" style="top:187px;">60420 Musterstadt am Main</div>
      <div class="contact-row" style="top:243px;">
        <svg viewBox="0 0 14 14"><path d="M3 0l2 3-1.5 2c1 2 3 4 5 5L10.5 8.5 14 10.5 12.5 14C6 14 0 8 0 1.5z"/></svg>
        <span>069 / 48 21 90</span>
      </div>
      <div class="contact-row" style="top:270px;">
        <svg viewBox="0 0 14 14"><path d="M7 1L0 7h2v6h4V9h2v4h4V7h2z"/></svg>
        <span>info@darvan-kueche.de</span>
      </div>
      <div class="contact-row" style="top:297px;">
        <svg viewBox="0 0 14 14"><path d="M0 3h14v8H0zM0 3l7 5 7-5"/></svg>
        <span>www.darvan-kueche.de</span>
      </div>
    </div>

    <div class="hours">
      <div class="hours-row"><span class="hours-day">Mo</span><span>11:30-22:30</span></div>
      <div class="hours-row"><span class="hours-day">D</span><span>11:30-22:30</span></div>
      <div class="hours-row"><span class="hours-day">Mi</span><span>11:30-22:30</span></div>
      <div class="hours-row"><span class="hours-day">D</span><span>11:30-22:30</span></div>
      <div class="hours-row"><span class="hours-day">F</span><span>11:30-22:30</span></div>
      <div class="hours-row"><span class="hours-day">Sa</span><span>12:00-22:30</span></div>
      <div class="hours-row"><span class="hours-day">So</span><span>12:00-22:30</span></div>
    </div>
  </section>
</body>
</html>
```